Schnapsbrennerei sucht neue Etiketten
Zielgruppe
Wir sind eine örtliche Schnapsbrennerei, die inzwischen seit ein paar Jahren einen eigenen Kundenstamm aufgebaut hat. Nun werden wir im nächsten Jahr einen neuen Verkaufsraum bauen. Aus diesem Grund wollen wir unsere Etiketten komplett überarbeiten.
Ein neues Logo habe ich bereits designen lassen. Diese finden Sie unten im Dokumententenupload. Wir legen viel Wert auf eine sehr hohe Qualität, welche sich sowohl in unserem Logo als auch den Etiketten Wiederspiegeln soll.
Unsere Kundschaft ist hauptsächlich Ü35 und legt viel Wert auf hochwertige Produkte.
Aufgabenstellung
Eines direkt vorne weg: Da wir unsere komplette Produktpalette neu gestalten wollen würde ich Sie bitten, der Einfachheit halber zuerst nur ein Schnapsetikett (z.B. Zwetschge oder Willi), ein Likör Etikett und ein Etikett für unseren Whiskey zu erstellen.
Darüber hinaus bitte ich Sie auch ein Design für unseren neuen Gin und einen Aquavit, welcher im Herbst auf den Markt kommen soll zu designen. Im Anschluss daran, werde ich in der Zusammenarbeit mit Ihnen die Etiketten optimieren wollen.
Sobald ein 'Grundetikett' entstanden ist, sollen dann auch die anderen Schnäpse und Liköre in dem gleichen Stil erstellt werden. Explizit möchte ich daraufhin weisen, dass sowohl die Whiskeys als auch der Gin und der Aquavit nicht zwangsläufig das gleiche 'Grundetikett' wie der Schnaps und der Likör haben sollen. Ist bei unseren aktuellen Etiketten auch nicht der Fall. Sehen Sie in den Bildern unten.
Wir verkaufen unseren Schnaps und Likör in 3 unterschieldichen Größen 0,2; 0,5 und 1,0 Liter. Wir verwenden für die 0,2 und 0,5 die Flasche Tessa. Das Etikett der 0,5er Flasche soll in etwa 65x120-130 mm sein. Hier sind wir allerdings variabel.
Dieses entstandene Etikett soll dann auf die anderen Flaschen entsprechend angepasst werden.
Sie finden im Dokumentenupload unsere aktuellen Etiketten und das Logo, welches eingebaut werden soll. Auch ein Etikett von einem örtlichen Weingut, welches mir vom Aufbau und der Unterteilung sehr gut gefällt, werde ich mit anhängen. Allerdings ist dieses Bild sehr unscharf. Wie gesagt es geht hierbei hauptsächlich um die Einteilung mit den oberen und den unteren 'Rahmen'.
Auch unsere Preisliste finden Sie Anhang, wobei diese noch in der Rohform ist und das Obst so nicht verwendet wird, aber hier sind die meisten Produkte drauf.
Das Logo gibt es in verschiedenen Farben. Gerne dürfen Sie für die unterschiedlichen Produkte auch unterschiedliche Farben nutzen.
Was ich mir persönlich g..

```html
<!DOCTYPE html>
<html lang="de">
<head>
<meta charset="utf-8">
<title>Wendler's Landbrennerei – Etiketten</title>
<link rel="stylesheet" href="https://fonts.googleapis.com/css2?family=Lato:wght@300;400;700&family=Dancing+Script:wght@500;600&display=swap">
<style>
  :root {
    --ink: #1d1d1d;
    --plum-bg: #a67e9e; --plum-band: #6a1a55; --plum-ink: #4f1a45;
    --herb-bg: #919e78; --herb-band: #3a5a26; --herb-ink: #2f4a20;
    --quince-bg: #f2ce98; --quince-band: #e39e23; --quince-ink: #d68e1e; --quince-art: #eab56a;
    --apple-bg: #dba59d; --apple-band: #c8665b; --apple-ink: #a9544a; --apple-art: #c98278;
    --whisky-dark-top: #62494b; --whisky-dark-band: #3a1f1f; --whisky-dark-ink: #c7b0a6;
    --whisky-light-top: #e1c7a7; --whisky-light-band: #c69d72; --whisky-light-ink: #8c6a4c;
    --whisky-se-top: #eadbc6; --whisky-se-band: #634a4c; --whisky-se-gold: #c89c72; --whisky-se-ink: #4a3a3a;
    --gin-grey: #575757; --gin-white: #ffffff; --gin-ink: #3c3c3c;
    --liqueur-top: #f6d2a8; --liqueur-mid: #eeae86; --liqueur-low: #e08e6c; --liqueur-deep: #c8714f;
    --whisky-amber: #e9893a; --whisky-deep: #c45a1e; --whisky-dark: #9c4212;
    --glass: #eeeae4; --cap: #1a1a1a; --cork: #c8a578;
  }
  * { box-sizing: border-box; margin: 0; padding: 0; }
  html, body { width: 848px; height: 1200px; overflow: hidden; background: #fff; }
  body { position: relative; font-family: "Lato", sans-serif; color: var(--ink); }
  .section-title { position: absolute; left: 50px; font-size: 16px; font-weight: 400; }
  .script { font-family: "Dancing Script", cursive; font-weight: 500; }

  .label { position: absolute; overflow: hidden; text-align: center; }
  .brand { position: absolute; left: 0; right: 0; display: flex; flex-direction: column; align-items: center; gap: 5px; }
  .brand-dot { width: 20px; height: 20px; border-radius: 50%; background: currentColor; opacity: .85; }
  .brand-name { font-weight: 700; letter-spacing: 1.6px; font-size: 7px; }

  /* tall liqueur labels */
  .label--tall { width: 176px; height: 325px; background: var(--bg); border: 0.5px solid rgba(0,0,0,.15); }
  .label--tall .brand { top: 10px; color: #fff; }
  .label--tall .band { position: absolute; left: 0; right: 0; top: 121px; height: 83px; background: var(--band); color: #fff; }
  .label--tall .maker { position: absolute; top: 10px; left: 0; right: 0; font-size: 12px; font-weight: 300; letter-spacing: .5px; }
  .label--tall .name { position: absolute; top: 24px; left: 0; right: 0; font-size: 46px; line-height: 1; }
  .label--tall .meta { position: absolute; left: 9px; right: 9px; top: 206px; display: flex; justify-content: space-between; font-size: 9px; font-weight: 300; color: var(--ink-c); }
  .label--tall .footer { position: absolute; left: 0; right: 0; bottom: 9px; font-size: 6px; line-height: 1.35; font-weight: 300; color: var(--ink-c); }
  .label--tall .fruit-art { position: absolute; left: 14px; right: 14px; top: 150px; height: 112px; border-radius: 45% 50% 45% 50%; background: radial-gradient(circle at 45% 45%, var(--quince-art), var(--quince-bg) 75%); }
  .label--quince .band { top: 73px; height: 86px; }
  .label--quince .meta { top: 282px; }
  .label--quince .brand { top: 12px; }

  .label--plum   { --bg: var(--plum-bg);   --band: var(--plum-band);   --ink-c: var(--plum-ink);   left: 50px;  top: 58px; }
  .label--herb   { --bg: var(--herb-bg);   --band: var(--herb-band);   --ink-c: var(--herb-ink);   left: 138px; top: 71px; transform: rotate(8.5deg); }
  .label--quince { --bg: var(--quince-bg); --band: var(--quince-band); --ink-c: var(--quince-ink); left: 234px; top: 71px; transform: rotate(2.5deg); }

  /* square whiskey labels */
  .label--square { width: 208px; height: 208px; background: var(--bg); border: 0.5px solid rgba(0,0,0,.25); }
  .label--square .brand { top: 8px; color: var(--logo); }
  .label--square .band { position: absolute; left: 0; right: 0; top: 61px; height: 91px; background: var(--band); }
  .label--square .maker { position: absolute; top: 5px; left: 0; right: 0; font-size: 11px; letter-spacing: .5px; color: var(--maker); }
  .label--square .name { position: absolute; top: 14px; left: 0; right: 0; font-size: 50px; line-height: 1; color: #fff; }
  .label--square .edition { position: absolute; top: 62px; left: 0; right: 0; font-size: 19px; line-height: 1; color: var(--edition); }
  .label--square .meta { position: absolute; left: 34px; right: 34px; top: 157px; display: flex; justify-content: space-between; font-size: 10px; font-weight: 300; color: var(--ink-c); }
  .label--square .footer { position: absolute; left: 0; right: 0; top: 177px; font-size: 6.8px; line-height: 1.35; font-weight: 300; color: var(--ink-c); }

  .label--dark  { --bg: var(--whisky-dark-top);  --band: var(--whisky-dark-band);  --logo: #fff; --maker: #8a7070; --edition: #a08080; --ink-c: var(--whisky-dark-ink); left: 50px;  top: 469px; }
  .label--light { --bg: var(--whisky-light-top); --band: var(--whisky-light-band); --logo: #e8a23a; --maker: #e4cbb0; --edition: #f2e2cf; --ink-c: var(--whisky-light-ink); left: 114px; top: 521px; }
  .label--special { --bg: var(--whisky-se-top); --band: var(--whisky-se-band); --logo: #e8a23a; --maker: #ecdcc7; --edition: var(--whisky-se-gold); --ink-c: var(--whisky-se-ink); left: 192px; top: 573px; }

  /* gin label */
  .label--gin { left: 50px; top: 846px; width: 282px; height: 282px; background: var(--gin-grey); border: 0.5px solid #444; }
  .label--gin .brand { top: 16px; color: #fff; gap: 9px; }
  .label--gin .brand-dot { width: 38px; height: 38px; }
  .label--gin .brand-name { font-size: 11px; letter-spacing: 2.5px; }
  .label--gin .panel { position: absolute; left: 73px; top: 114px; width: 136px; height: 126px; background: var(--gin-white); color: var(--gin-ink); }
  .label--gin .maker { position: absolute; top: 14px; left: 0; right: 0; font-size: 18px; font-weight: 300; letter-spacing: .5px; }
  .label--gin .name { position: absolute; top: 34px; left: 0; right: 0; font-size: 70px; line-height: 1; }
  .label--gin .vol { position: absolute; bottom: 46px; font-size: 12px; font-weight: 300; color: #fff; }
  .label--gin .vol--left { left: 14px; } .label--gin .vol--right { right: 14px; }
  .label--gin .strip { position: absolute; left: 0; right: 0; bottom: 0; height: 42px; background: var(--gin-white); color: var(--gin-ink); font-size: 9.5px; line-height: 1.2; font-weight: 300; padding-top: 8px; }

  /* bottles */
  .bottle { position: absolute; }
  .bottle-cap, .bottle-neck, .bottle-body, .bottle-cork { position: absolute; display: block; }
  .bottle-cap { background: linear-gradient(90deg, #0d0d0d, #2e2e2e 45%, #0d0d0d); border-radius: 3px 3px 0 0; }

  .bottle--liqueur { top: 74px; width: 64px; height: 280px; }
  .bottle--liqueur .bottle-body { left: 0; top: 84px; width: 64px; height: 196px; border-radius: 30px 30px 6px 6px;
    background: linear-gradient(90deg, rgba(0,0,0,.12), rgba(255,255,255,.15) 30%, rgba(0,0,0,0) 60%, rgba(0,0,0,.14)),
                linear-gradient(180deg, var(--liqueur-top), var(--liqueur-mid) 40%, var(--liqueur-low) 80%, var(--liqueur-deep)); }
  .bottle--liqueur .bottle-neck { left: 20px; top: 58px; width: 24px; height: 40px; background: linear-gradient(180deg, var(--glass), var(--liqueur-top)); }
  .bottle--liqueur .bottle-cap { left: 19px; top: 0; width: 26px; height: 60px; }

  .bottle--whiskey { top: 491px; width: 108px; height: 284px; }
  .bottle--whiskey .bottle-body { left: 0; top: 78px; width: 108px; height: 206px; border-radius: 28px 28px 10px 10px;
    background: linear-gradient(90deg, rgba(0,0,0,.18), rgba(255,255,255,.12) 25%, rgba(0,0,0,0) 60%, rgba(0,0,0,.2)),
                linear-gradient(180deg, var(--whisky-amber), var(--whisky-deep) 60%, var(--whisky-dark)); }
  .bottle--whiskey .bottle-neck { left: 34px; top: 52px; width: 40px; height: 34px; background: linear-gradient(180deg, #d9b48c, var(--whisky-amber)); }
  .bottle--whiskey .bottle-cap { left: 32px; top: 0; width: 44px; height: 55px; }

  .gin-scene { position: absolute; left: 417px; top: 850px; width: 372px; height: 280px; background: linear-gradient(180deg, #f4f4f4, #e8e8e8 78%, #f7f7f7); }
  .bottle--gin { left: 142px; top: 40px; width: 88px; height: 211px; }
  .bottle--gin .bottle-body { left: 0; top: 46px; width: 88px; height: 165px; border-radius: 22px 22px 8px 8px; border: 1px solid #c9c9c9;
    background: linear-gradient(90deg, rgba(200,200,200,.55), rgba(255,255,255,.7) 30%, rgba(240,240,240,.4) 65%, rgba(190,190,190,.55)); }
  .bottle--gin .bottle-cork { left: 27px; top: 14px; width: 34px; height: 36px; background: var(--cork); border-left: 1px solid #b9b9b9; border-right: 1px solid #b9b9b9; }
  .bottle--gin .bottle-cap { left: 24px; top: 0; width: 40px; height: 16px; border-radius: 4px; }

  /* labels as applied on bottles */
  .mini { position: absolute; overflow: hidden; text-align: center; background: var(--bg); }
  .mini .brand { gap: 1px; }
  .mini .footer, .mini .meta { font-weight: 300; color: var(--ink-c); }

  .mini--liqueur { left: 7px; top: 129px; width: 50px; height: 96px; }
  .mini--liqueur .brand { top: 3px; color: #fff; }
  .mini--liqueur .brand-dot { width: 6px; height: 6px; }
  .mini--liqueur .brand-name { font-size: 2.4px; letter-spacing: .4px; }
  .mini--liqueur .band { position: absolute; left: 0; right: 0; top: 36px; height: 20px; background: var(--band); color: #fff; }
  .mini--liqueur .maker { position: absolute; top: 1.5px; left: 0; right: 0; font-size: 3.2px; font-weight: 300; }
  .mini--liqueur .name { position: absolute; top: 5px; left: 0; right: 0; font-size: 11.5px; line-height: 1; }
  .mini--liqueur .meta { position: absolute; left: 3px; right: 3px; top: 58px; display: flex; justify-content: space-between; font-size: 2.6px; }
  .mini--liqueur .footer { position: absolute; left: 0; right: 0; bottom: 3px; font-size: 1.9px; line-height: 1.3; }
  .mini--liqueur .fruit-art { position: absolute; left: 8px; right: 8px; top: 50px; height: 30px; border-radius: 45%; background: radial-gradient(circle, var(--art), var(--bg) 75%); }
  .mini--fruit .band { top: 23px; height: 24px; }
  .mini--fruit .name { top: 7px; font-size: 12px; }
  .mini--fruit .meta { top: 82px; }
  .mini--plum { --bg: var(--plum-bg); --band: var(--plum-band); --ink-c: var(--plum-ink); }
  .mini--herb { --bg: var(--herb-bg); --band: var(--herb-band); --ink-c: var(--herb-ink); }
  .mini--quince { --bg: var(--quince-bg); --band: var(--quince-band); --ink-c: var(--quince-ink); --art: var(--quince-art); }
  .mini--apple { --bg: var(--apple-bg); --band: var(--apple-band); --ink-c: var(--apple-ink); --art: var(--apple-art); }

  .mini--whiskey { left: 5px; top: 135px; width: 98px; height: 112px; }
  .mini--whiskey .brand { top: 4px; color: var(--logo); }
  .mini--whiskey .brand-dot { width: 9px; height: 9px; }
  .mini--whiskey .brand-name { font-size: 3.4px; letter-spacing: .6px; }
  .mini--whiskey .band { position: absolute; left: 0; right: 0; top: 32px; height: 51px; background: var(--band); }
  .mini--whiskey .maker { position: absolute; top: 3px; left: 0; right: 0; font-size: 5.4px; color: var(--maker); }
  .mini--whiskey .name { position: absolute; top: 9px; left: 0; right: 0; font-size: 24px; line-height: 1; color: #fff; }
  .mini--whiskey .edition { position: absolute; top: 35px; left: 0; right: 0; font-size: 10px; line-height: 1; color: var(--edition); }
  .mini--whiskey .meta { position: absolute; left: 11px; right: 11px; top: 85px; display: flex; justify-content: space-between; font-size: 5px; }
  .mini--whiskey .footer { position: absolute; left: 0; right: 0; top: 95px; font-size: 3.3px; line-height: 1.35; }
  .mini--dark { --bg: var(--whisky-dark-top); --band: var(--whisky-dark-band); --logo: #fff; --maker: #8a7070; --edition: #a08080; --ink-c: var(--whisky-dark-ink); }
  .mini--light { --bg: var(--whisky-light-top); --band: var(--whisky-light-band); --logo: #e8a23a; --maker: #e4cbb0; --edition: #f2e2cf; --ink-c: var(--whisky-light-ink); }
  .mini--special { --bg: var(--whisky-se-top); --band: var(--whisky-se-band); --logo: #e8a23a; --maker: #ecdcc7; --edition: var(--whisky-se-gold); --ink-c: var(--whisky-se-ink); }

  .mini--gin { left: 12px; top: 107px; width: 64px; height: 65px; background: var(--gin-grey); }
  .mini--gin .brand { top: 4px; color: #fff; }
  .mini--gin .brand-dot { width: 8px; height: 8px; }
  .mini--gin .brand-name { font-size: 2.6px; letter-spacing: .5px; }
  .mini--gin .panel { position: absolute; left: 17px; top: 26px; width: 30px; height: 29px; background: var(--gin-white); color: var(--gin-ink); }
  .mini--gin .maker { position: absolute; top: 3px; left: 0; right: 0; font-size: 4px; font-weight: 300; }
  .mini--gin .name { position: absolute; top: 8px; left: 0; right: 0; font-size: 15px; line-height: 1; }
  .mini--gin .vol { position: absolute; top: 49px; font-size: 2.8px; font-weight: 300; color: #fff; }
  .mini--gin .vol--left { left: 3px; } .mini--gin .vol--right { right: 3px; }
  .mini--gin .strip { position: absolute; left: 0; right: 0; bottom: 0; height: 10px; background: var(--gin-white); color: var(--gin-ink); font-size: 2.1px; line-height: 1.25; font-weight: 300; padding-top: 2px; }
</style>
</head>
<body>

<h2 class="section-title" style="top:22px">Liköre/Schnäpse:</h2>

<div class="label label--tall label--plum">
  <div class="brand"><span class="brand-dot"></span><span class="brand-name">WENDLER'S</span></div>
  <div class="band"><div class="maker">WENDLER'S</div><div class="name script">Pflaume</div></div>
  <div class="meta"><span>40 % VOL</span><span>0,2 L</span></div>
  <div class="footer">Edelbrände &amp; Liköre Konrad Wendler<br>Lindenweg 12 · D-97340 Mainbach · Telefon 0 93 40-12 58</div>
</div>

<div class="label label--tall label--herb">
  <div class="brand"><span class="brand-dot"></span><span class="brand-name">WENDLER'S</span></div>
  <div class="band"><div class="maker">WENDLER'S</div><div class="name script">Kräuter</div></div>
  <div class="meta"><span>40 % VOL</span><span>0,2 L</span></div>
  <div class="footer">Edelbrände &amp; Liköre Konrad Wendler<br>Lindenweg 12 · D-97340 Mainbach · Telefon 0 93 40-12 58</div>
</div>

<div class="label label--tall label--quince">
  <div class="brand"><span class="brand-dot"></span><span class="brand-name">WENDLER'S</span></div>
  <div class="fruit-art" role="img" aria-label="Zeichnung zweier Quitten mit Blatt"></div>
  <div class="band"><div class="maker">WENDLER'S</div><div class="name script">Quitte</div></div>
  <div class="meta"><span>40 % VOL</span><span>0,2 L</span></div>
  <div class="footer">Edelbrände &amp; Liköre Konrad Wendler<br>Lindenweg 12 · D-97340 Mainbach · Telefon 0 93 40-12 58</div>
</div>

<div class="bottle bottle--liqueur" style="left:444px">
  <span class="bottle-body"></span><span class="bottle-neck"></span><span class="bottle-cap"></span>
  <div class="mini mini--liqueur mini--plum">
    <div class="brand"><span class="brand-dot"></span><span class="brand-name">WENDLER'S</span></div>
    <div class="band"><div class="maker">WENDLER'S</div><div class="name script">Pflaume</div></div>
    <div class="meta"><span>40 % VOL</span><span>0,2 L</span></div>
    <div class="footer">Edelbrände &amp; Liköre Konrad Wendler<br>Lindenweg 12 · Mainbach · 0 93 40-12 58</div>
  </div>
</div>

<div class="bottle bottle--liqueur" style="left:539px">
  <span class="bottle-body"></span><span class="bottle-neck"></span><span class="bottle-cap"></span>
  <div class="mini mini--liqueur mini--herb">
    <div class="brand"><span class="brand-dot"></span><span class="brand-name">WENDLER'S</span></div>
    <div class="band"><div class="maker">WENDLER'S</div><div class="name script">Kräuter</div></div>
    <div class="meta"><span>40 % VOL</span><span>0,2 L</span></div>
    <div class="footer">Edelbrände &amp; Liköre Konrad Wendler<br>Lindenweg 12 · Mainbach · 0 93 40-12 58</div>
  </div>
</div>

<div class="bottle bottle--liqueur" style="left:634px">
  <span class="bottle-body"></span><span class="bottle-neck"></span><span class="bottle-cap"></span>
  <div class="mini mini--liqueur mini--fruit mini--quince">
    <div class="brand"><span class="brand-dot"></span><span class="brand-name">WENDLER'S</span></div>
    <div class="fruit-art" role="img" aria-label="Zeichnung zweier Quitten"></div>
    <div class="band"><div class="maker">WENDLER'S</div><div class="name script">Quitte</div></div>
    <div class="meta"><span>40 % VOL</span><span>0,2 L</span></div>
    <div class="footer">Edelbrände &amp; Liköre Konrad Wendler<br>Lindenweg 12 · Mainbach · 0 93 40-12 58</div>
  </div>
</div>

<div class="bottle bottle--liqueur" style="left:729px">
  <span class="bottle-body"></span><span class="bottle-neck"></span><span class="bottle-cap"></span>
  <div class="mini mini--liqueur mini--fruit mini--apple">
    <div class="brand"><span class="brand-dot"></span><span class="brand-name">WENDLER'S</span></div>
    <div class="fruit-art" role="img" aria-label="Zeichnung eines Apfels"></div>
    <div class="band"><div class="maker">WENDLER'S</div><div class="name script">Apfel</div></div>
    <div class="meta"><span>40 % VOL</span><span>0,2 L</span></div>
    <div class="footer">Edelbrände &amp; Liköre Konrad Wendler<br>Lindenweg 12 · Mainbach · 0 93 40-12 58</div>
  </div>
</div>

<h2 class="section-title" style="top:429px">Whiskey:</h2>

<div class="label label--square label--dark">
  <div class="brand"><span class="brand-dot"></span><span class="brand-name">WENDLER'S</span></div>
  <div class="band"><div class="maker">WENDLER'S</div><div class="name script">Whiskey</div><div class="edition script">dunkel</div></div>
  <div class="meta"><span>40 % VOL</span><span>0,2 L</span></div>
  <div class="footer">Edelbrände &amp; Liköre Konrad Wendler<br>Lindenweg 12 · D-97340 Mainbach · Telefon 0 93 40-12 58</div>
</div>

<div class="label label--square label--light">
  <div class="brand"><span class="brand-dot"></span><span class="brand-name">WENDLER'S</span></div>
  <div class="band"><div class="maker">WENDLER'S</div><div class="name script">Whiskey</div><div class="edition script">hell</div></div>
  <div class="meta"><span>40 % VOL</span><span>0,2 L</span></div>
  <div class="footer">Edelbrände &amp; Liköre Konrad Wendler<br>Lindenweg 12 · D-97340 Mainbach · Telefon 0 93 40-12 58</div>
</div>

<div class="label label--square label--special">
  <div class="brand"><span class="brand-dot"></span><span class="brand-name">WENDLER'S</span></div>
  <div class="band"><div class="maker">WENDLER'S</div><div class="name script">Whiskey</div><div class="edition script">Special Edition</div></div>
  <div class="meta"><span>40 % VOL</span><span>0,2 L</span></div>
  <div class="footer">Edelbrände &amp; Liköre Konrad Wendler<br>Lindenweg 12 · D-97340 Mainbach · Telefon 0 93 40-12 58</div>
</div>

<div class="bottle bottle--whiskey" style="left:430px">
  <span class="bottle-body"></span><span class="bottle-neck"></span><span class="bottle-cap"></span>
  <div class="mini mini--whiskey mini--dark">
    <div class="brand"><span class="brand-dot"></span><span class="brand-name">WENDLER'S</span></div>
    <div class="band"><div class="maker">WENDLER'S</div><div class="name script">Whiskey</div><div class="edition script">dunkel</div></div>
    <div class="meta"><span>40 % VOL</span><span>0,2 L</span></div>
    <div class="footer">Edelbrände &amp; Liköre Konrad Wendler<br>Lindenweg 12 · D-97340 Mainbach · Telefon 0 93 40-12 58</div>
  </div>
</div>

<div class="bottle bottle--whiskey" style="left:558px">
  <span class="bottle-body"></span><span class="bottle-neck"></span><span class="bottle-cap"></span>
  <div class="mini mini--whiskey mini--light">
    <div class="brand"><span class="brand-dot"></span><span class="brand-name">WENDLER'S</span></div>
    <div class="band"><div class="maker">WENDLER'S</div><div class="name script">Whiskey</div><div class="edition script">hell</div></div>
    <div class="meta"><span>40 % VOL</span><span>0,2 L</span></div>
    <div class="footer">Edelbrände &amp; Liköre Konrad Wendler<br>Lindenweg 12 · D-97340 Mainbach · Telefon 0 93 40-12 58</div>
  </div>
</div>

<div class="bottle bottle--whiskey" style="left:685px">
  <span class="bottle-body"></span><span class="bottle-neck"></span><span class="bottle-cap"></span>
  <div class="mini mini--whiskey mini--special">
    <div class="brand"><span class="brand-dot"></span><span class="brand-name">WENDLER'S</span></div>
    <div class="band"><div class="maker">WENDLER'S</div><div class="name script">Whiskey</div><div class="edition script">Special Edition</div></div>
    <div class="meta"><span>40 % VOL</span><span>0,2 L</span></div>
    <div class="footer">Edelbrände &amp; Liköre Konrad Wendler<br>Lindenweg 12 · D-97340 Mainbach · Telefon 0 93 40-12 58</div>
  </div>
</div>

<h2 class="section-title" style="top:806px">Whiskey:</h2>

<div class="label label--gin">
  <div class="brand"><span class="brand-dot"></span><span class="brand-name">WENDLER'S</span></div>
  <div class="panel"><div class="maker">WENDLER'S</div><div class="name script">Gin</div></div>
  <span class="vol vol--left">40 % VOL</span>
  <span class="vol vol--right">0,2 L</span>
  <div class="strip">Edelbrände &amp; Liköre Konrad Wendler<br>Lindenweg 12 · D-97340 Mainbach · Telefon 0 93 40-12 58</div>
</div>

<div class="gin-scene">
  <div class="bottle bottle--gin">
    <span class="bottle-body"></span><span class="bottle-cork"></span><span class="bottle-cap"></span>
    <div class="mini mini--gin">
      <div class="brand"><span class="brand-dot"></span><span class="brand-name">WENDLER'S</span></div>
      <div class="panel"><div class="maker">WENDLER'S</div><div class="name script">Gin</div></div>
      <span class="vol vol--left">40 % VOL</span>
      <span class="vol vol--right">0,2 L</span>
      <div class="strip">Edelbrände &amp; Liköre Konrad Wendler<br>Lindenweg 12 · Mainbach · 0 93 40-12 58</div>
    </div>
  </div>
</div>

</body>
</html>
```